Dental Magazine Cover

I need a template created for a magazine cover. Magazine title is "Dentistry Halvern"

I would like to have a logo designed for "Dentistry Halvern"

For each issue, we would like to keep the same basic template and change out the photos, text, etc. according to the contents of the issue.

You can create the cover of the first issue with the attached photos and captions:

Date for use on magazine cover is February 2014

Main caption: Maxillary Reconstruction with Immediately Loaded Dental Implants
(Use attached File 1 for main photo. Photo may be cropped and rotated as needed)

Inset: Bisphosphonate Guidelines for Dental Treatment
(Use attached file 2 for inset photo. Photo may be cropped and rotated as needed).

Target Market(s)

Target audience for this magazine are dentists, dental hygienists, dental assistants, and dental professionals in the Austin, Texas area.

Industry/Entity Type

Dental

Other font styles liked:
• Font need to "POP"

Requirements
Must have
• Please see project overview guidelines. Magazine cover needs to have the following:
1) Logo
2) Main image
3) Caption for Main image (Maxillary Reconstruction with Immediately Loaded Dental Implants)
4) Smaller Inset Photo
5) Caption for smaller inset photo (Bisphosphonate Guidelines for Dental Treatment)
6) Date of magazine issue (February 2014)

Use any of the Photos you see fit to make the magazine cover work.
Nice to have
• Please try to make the "Dentistry Halvern" logo "POP". Dental journals are boring enough. We can at least have a logo that pops. Simply using generic text will win this design. The below text is just a suggestion of a Logo. Please feel free to use all creative license in making a logo that has some sizzle. PLEASE NOTE: A tooth is NOT needed in the logo...

```html
<!DOCTYPE html>
<html lang="en">
<head>
<meta charset="utf-8">
<title>Dentistry Halvern – February 2014 Cover</title>
<link href="https://fonts.googleapis.com/css2?family=Oswald:wght@400;700&display=swap" rel="stylesheet">
<style>
  :root{
    --stage:#9a9a9a;
    --header-grey:#cfcfcf;
    --rule-grey:#b5b5b5;
    --ink:#2a2a2a;
    --muted:#a9a9a9;
    --orange:#f5a623;
    --magenta:#a4336f;
    --white:#ffffff;
    --bone-teal:#4fc8b0;
    --bone-pink:#d05aa8;
    --bone-gold:#e3b75a;
    --void:#0d0d10;
  }
  *{box-sizing:border-box;margin:0;padding:0}
  html,body{width:1200px;height:900px;overflow:hidden}
  body{
    background:radial-gradient(ellipse at 50% 45%,#dcdcdc 0%,#a8a8a8 55%,#6f6f6f 100%);
    font-family:"Oswald",sans-serif;
    position:relative;
  }
  .cover{
    position:absolute;left:330px;top:70px;width:540px;height:760px;
    background:var(--white);
    border-left:7px solid var(--orange);
    box-shadow:0 20px 40px rgba(0,0,0,.35);
    overflow:hidden;
  }
  .masthead{
    position:absolute;left:0;top:0;width:100%;height:178px;
    background:linear-gradient(to bottom,var(--header-grey) 0,var(--header-grey) 118px,var(--white) 118px);
    border-bottom:4px solid var(--rule-grey);
    display:flex;align-items:center;justify-content:center;gap:14px;
  }
  .masthead__dot{width:18px;height:18px;border-radius:50%;background:var(--orange)}
  .masthead__title{
    font-weight:700;font-size:50px;line-height:1;color:var(--ink);
    text-transform:uppercase;letter-spacing:1px;
  }
  .issue-line{
    position:absolute;left:0;top:182px;width:100%;height:36px;
    display:flex;align-items:center;justify-content:space-between;padding:0 18px 0 14px;
  }
  .issue-line__audience{font-size:13px;color:var(--muted);font-weight:700;letter-spacing:.2px}
  .issue-line__date{font-size:21px;color:var(--orange);font-weight:700}
  .cover-photo{
    position:absolute;left:0;top:222px;width:100%;height:476px;
    background:
      radial-gradient(circle at 20% 25%,var(--bone-teal) 0,transparent 28%),
      radial-gradient(circle at 75% 20%,var(--bone-pink) 0,transparent 30%),
      radial-gradient(circle at 60% 65%,var(--bone-teal) 0,transparent 26%),
      radial-gradient(circle at 30% 80%,var(--bone-pink) 0,transparent 30%),
      radial-gradient(circle at 85% 85%,var(--bone-gold) 0,transparent 25%),
      var(--void);
  }
  .feature-tab{
    position:absolute;right:0;top:310px;width:282px;height:84px;
    background:var(--magenta);
    border-radius:42px 0 0 42px;
    border:2px solid rgba(255,255,255,.7);border-right:none;
    padding:8px 12px 8px 26px;
    color:var(--white);font-weight:700;font-size:17px;line-height:1.15;
  }
  .inset{
    position:absolute;left:48px;top:470px;width:196px;height:196px;border-radius:50%;
    background:var(--white);border:6px solid var(--magenta);
    box-shadow:0 0 0 4px var(--white);
    overflow:hidden;text-align:center;
  }
  .inset__photo{
    position:absolute;left:22px;top:34px;width:140px;height:62px;border-radius:8px;
    background:linear-gradient(to bottom,#b58a4e,#e6d1a6 60%,#6e5431);
  }
  .inset__caption{
    position:absolute;left:0;top:104px;width:100%;color:var(--ink);font-weight:700;line-height:1.05;
  }
  .inset__caption .big{display:block;font-size:15px}
  .inset__caption .small{display:block;font-size:9px;font-weight:400}
  .footer{
    position:absolute;left:0;bottom:0;width:100%;height:62px;
    display:flex;align-items:center;justify-content:center;
    font-weight:700;font-size:19px;letter-spacing:5px;color:var(--ink);
  }
</style>
</head>
<body>
  <main class="cover">
    <header class="masthead">
      <span class="masthead__dot"></span>
      <h1 class="masthead__title">Dentistry Halvern</h1>
    </header>
    <div class="issue-line">
      <span class="issue-line__audience">magazine are dentists, dental hygienists, dental assistants</span>
      <span class="issue-line__date">February 2014</span>
    </div>
    <div class="cover-photo" role="img" aria-label="Main photo: colourful micrograph of trabecular bone structure"></div>
    <div class="feature-tab">Maxillary Reconstruction<br>with Immediately<br>loaded Dental Implants</div>
    <div class="inset">
      <div class="inset__photo" role="img" aria-label="Inset photo: dental model of upper teeth"></div>
      <p class="inset__caption">
        <span class="big">Bisphosphonate</span>
        <span class="small">Guidelines for</span>
        <span class="big">Dental Treatment</span>
      </p>
    </div>
    <footer class="footer">www.dentistryhalvern-mag.org</footer>
  </main>
</body>
</html>
```